Luxury Brand Real Estate For Sale sign

**Update** I've added some examples from the internet of other signs that have a look similar to what I would like to see. I do not want my personal name in the sign. And the word FOR SALE Does not need to be so large - it can be more subtle.
I want to create a Real Estate for sale sign for my company that will be used for luxury/higher end real estate listings. I’m sharing my business card as well as a logo with new teal color to show what we're moving towards: we’re using Teal, white, black and gold.
Hoping the sign is simple, sophisticated and eye catching.
The sign should be 24" wide by 30" tall including the company name: Harbor Crest Realty Group and our logo, office phone number 727-555-0148 and website www.hcrgexample.com the words "For Sale"
Optional to add this e-mail address info@hcrgexample.com to the sign
Target Market(s)
Luxury home buyers
Industry/Entity Type
Real Estate
Look and feel

```html
<!DOCTYPE html>
<html lang="en">
<head>
<meta charset="utf-8">
<title>HCRG For Sale Sign</title>
<link rel="stylesheet" href="https://fonts.googleapis.com/css2?family=Montserrat:wght@300&family=Open+Sans:wght@700&display=swap">
<style>
  :root {
    --teal: #108c86;
    --teal-deep: #0b6f6b;
    --gold: #b28e1e;
    --white: #ffffff;
    --backdrop: #eef0ef;
  }
  * { margin: 0; padding: 0; box-sizing: border-box; }
  html, body { width: 1200px; height: 1200px; overflow: hidden; }
  body {
    background: var(--backdrop);
    position: relative;
    font-family: "Open Sans", Arial, sans-serif;
  }
  .sign {
    position: absolute;
    left: 228px;
    top: 62px;
    width: 744px;
    height: 1076px;
    background: var(--teal);
    overflow: hidden;
    box-shadow: 0 10px 30px rgba(0,0,0,0.18);
  }
  .brand {
    position: absolute;
    left: 50%;
    top: 40px;
    transform: translateX(-50%);
    display: flex;
    align-items: center;
    gap: 18px;
  }
  .brand-square {
    width: 22px;
    height: 22px;
    background: var(--white);
  }
  .brand-name {
    font-family: "Montserrat", Arial, sans-serif;
    font-weight: 300;
    font-size: 104px;
    letter-spacing: 2px;
    color: var(--white);
    line-height: 1;
  }
  .status-band {
    position: absolute;
    left: 0;
    top: 206px;
    width: 100%;
    height: 158px;
    background: var(--gold);
    display: flex;
    align-items: center;
    justify-content: center;
  }
  .status-text {
    font-weight: 700;
    font-size: 112px;
    color: var(--white);
    letter-spacing: 2px;
    line-height: 1;
  }
  .area-photo {
    position: absolute;
    left: 0;
    top: 364px;
    width: 100%;
    height: 472px;
    background: linear-gradient(160deg, #3f8f8c 0%, #7fc1bd 35%, #2e7c79 65%, #1d5f5d 100%);
  }
  .gold-rule {
    position: absolute;
    left: 0;
    top: 836px;
    width: 100%;
    height: 9px;
    background: var(--gold);
  }
  .contact {
    position: absolute;
    left: 0;
    top: 845px;
    width: 100%;
    height: 231px;
    display: flex;
    flex-direction: column;
    align-items: center;
    justify-content: center;
    gap: 18px;
    color: var(--white);
  }
  .contact-line {
    display: flex;
    align-items: center;
    gap: 14px;
    font-weight: 700;
    font-size: 58px;
    line-height: 1;
  }
  .contact-icon { width: 40px; height: 40px; flex: none; }
</style>
</head>
<body>
  <div class="sign">
    <div class="brand">
      <span class="brand-square"></span>
      <span class="brand-name">HCRG</span>
    </div>

    <div class="status-band">
      <span class="status-text">FOR SALE</span>
    </div>

    <div class="area-photo" role="img" aria-label="Aerial photograph of a waterfront city skyline along a channel, tinted teal"></div>

    <div class="gold-rule"></div>

    <div class="contact">
      <div class="contact-line">
        <svg class="contact-icon" viewBox="0 0 24 24" fill="none" stroke="#ffffff" stroke-width="1.8" stroke-linejoin="round">
          <path d="M5 3h4l2 5-2.5 1.5a11 11 0 0 0 6 6L16 13l5 2v4a2 2 0 0 1-2 2A16 16 0 0 1 3 5a2 2 0 0 1 2-2z"/>
        </svg>
        <span class="phone">727-555-0148</span>
      </div>
      <div class="contact-line">
        <svg class="contact-icon" viewBox="0 0 24 24" fill="none" stroke="#ffffff" stroke-width="1.8" stroke-linejoin="round">
          <path d="M4 3l15 7-6 2-2 6z"/>
          <path d="M13 12l6 6"/>
        </svg>
        <span class="website">hcrgexample.com</span>
      </div>
    </div>
  </div>
</body>
</html>
```